Now Leasing Banner

Looking for a banner that says the following information approx 4' x 30'

Now Leasing Maplewood Terrace 925-318-6054

Target Market(s)

Drive by traffic

Industry/Entity Type

Residential property management

Requirements
Must have
• Clear and readable from a distance

```html
<!DOCTYPE html>
<html lang="en">
<head>
<meta charset="utf-8">
<title>Now Leasing Banner</title>
<link href="https://fonts.googleapis.com/css2?family=Montserrat:wght@400;600;700;800&display=swap" rel="stylesheet">
<style>
  :root {
    --page: #eef0f3;
    --navy: #1b2a55;
    --navy-deep: #13204a;
    --teal: #10707a;
    --white: #ffffff;
    --ink: #1b2a55;
    --gray-dark: #3a3a3c;
    --gray-mid: #77787c;
    --scenery: 29, 106, 120;
  }
  * { box-sizing: border-box; margin: 0; padding: 0; }
  html, body {
    width: 1200px; height: 800px; overflow: hidden;
    background: var(--page);
    font-family: "Montserrat", Arial, sans-serif;
  }
  .banner {
    position: absolute; left: 20px; top: 326px;
    width: 1160px; height: 147px;
    background: var(--white);
    border: 5px solid var(--white);
    box-shadow: 0 2px 10px rgba(0,0,0,.15);
    overflow: hidden;
  }
  .banner-inner { position: relative; width: 100%; height: 100%; }

  .intro-panel {
    position: absolute; left: 0; top: 0; width: 283px; height: 100%;
    background: linear-gradient(100deg, var(--navy-deep) 0%, var(--navy) 55%, #2d3f6e 100%);
  }
  .intro-text {
    position: absolute; left: 36px; top: 17px; color: var(--white); line-height: 1;
  }
  .intro-kicker { font-weight: 400; font-size: 18px; letter-spacing: .3px; }
  .intro-headline {
    font-weight: 800; font-size: 42px; letter-spacing: -2px; line-height: .9; margin-top: 3px;
  }
  .intro-tagline { font-weight: 400; font-size: 13.5px; margin-top: 4px; letter-spacing: .3px; }
  .intro-tagline strong { font-weight: 700; }

  .room-photo { position: absolute; left: 224px; top: 0; width: 142px; height: 137px; }

  .scenery-band {
    position: absolute; left: 364px; bottom: 0; width: 400px; height: 16px;
    background: linear-gradient(90deg, rgba(var(--scenery), .75), rgba(var(--scenery), .35) 65%, rgba(var(--scenery), 0));
  }

  .headline-pill {
    position: absolute; left: 390px; top: 42px; height: 57px; width: 348px;
    display: flex; border-radius: 29px; overflow: hidden;
  }
  .pill-now, .pill-leasing {
    display: flex; align-items: center; color: var(--white);
    font-weight: 800; font-size: 40px; letter-spacing: -1.5px;
  }
  .pill-now { background: var(--teal); padding: 0 8px 0 22px; }
  .pill-leasing { background: var(--navy); flex: 1; padding-left: 6px; }
  .property-name {
    position: absolute; left: 380px; top: 104px; width: 368px; text-align: center;
    color: var(--ink); font-weight: 700; font-size: 23px; letter-spacing: -1.2px; line-height: 1.1;
  }

  .contact-photo {
    position: absolute; right: 0; top: 0; width: 460px; height: 100%;
    background: linear-gradient(90deg, rgba(255,255,255,0) 0%, var(--gray-mid) 18%, #525356 45%, var(--gray-dark) 100%);
  }
  .contact {
    position: absolute; left: 842px; top: 54px; display: flex; align-items: center; gap: 12px;
    color: var(--white);
  }
  .phone-icon { width: 28px; height: 28px; margin-top: -14px; }
  .contact-label { font-weight: 600; font-size: 15px; letter-spacing: .8px; line-height: 1; }
  .contact-number { font-weight: 600; font-size: 32px; letter-spacing: .5px; line-height: 1.05; }
</style>
</head>
<body>
  <section class="banner" aria-label="Now Leasing Maplewood Terrace banner">
    <div class="banner-inner">
      <div class="intro-panel" role="img" aria-label="Photo of a modern apartment building in navy tones"></div>
      <div class="intro-text">
        <p class="intro-kicker">FIND YOUR</p>
        <p class="intro-headline">DREAM<br>HOUSE</p>
        <p class="intro-tagline">WITH <strong>LOW PRICE</strong></p>
      </div>

      <svg class="room-photo" viewBox="0 0 142 137" role="img" aria-label="Photo of a bright furnished living room">
        <defs>
          <linearGradient id="roomTone" x1="0" y1="0" x2="0" y2="1">
            <stop offset="0" stop-color="#e9edf3"/>
            <stop offset=".55" stop-color="#c9d0dc"/>
            <stop offset="1" stop-color="#4a5a7c"/>
          </linearGradient>
        </defs>
        <polygon points="38,4 104,4 138,68.5 104,133 38,133 4,68.5" fill="url(#roomTone)" stroke="#ffffff" stroke-width="6"/>
      </svg>

      <div class="scenery-band" role="img" aria-label="Teal mountain landscape illustration"></div>

      <div class="headline-pill">
        <span class="pill-now">NOW</span>
        <span class="pill-leasing">LEASING</span>
      </div>
      <p class="property-name">MAPLEWOOD TERRACE</p>

      <div class="contact-photo" role="img" aria-label="Photo of an agent holding a glowing house symbol and handing over keys"></div>
      <div class="contact">
        <svg class="phone-icon" viewBox="0 0 28 28" aria-hidden="true">
          <circle cx="14" cy="14" r="12.5" fill="none" stroke="#ffffff" stroke-width="1.4"/>
          <path d="M9.5 7.5c.8-.5 1.6-.3 2 .4l1.2 2.2c.4.7.2 1.4-.4 1.8l-.9.6c.7 1.8 2 3.2 3.8 4l.6-.9c.4-.6 1.2-.8 1.8-.4l2.2 1.2c.7.4.9 1.3.4 2l-.8 1.1c-.6.8-1.6 1.1-2.6.8-4.3-1.4-7.3-4.5-8.6-8.7-.3-1 .1-2 .9-2.6z" fill="none" stroke="#ffffff" stroke-width="1.3"/>
        </svg>
        <div>
          <p class="contact-label">BOOK NOW</p>
          <p class="contact-number">925-318-6054</p>
        </div>
      </div>
    </div>
  </section>
</body>
</html>
```